Letterhead Design Project

Letterhead for a Consultant Cardiologist in Adelaide Australia. Should be very classy, mature and imposing. I would prefer colours that portray confidence, gentleness and serenity.

The PDF attached is for you to see the details that will be on the letterhead and not the design which is extremely poor!

Target Market(s)

Health professionals especially medical doctors

Industry/Entity Type

Consultant

```html
<!DOCTYPE html>
<html lang="en">
<head>
<meta charset="utf-8">
<title>Letterhead – Dr Adaeze O. Nwankwo, Cardiologist</title>
<link href="https://fonts.googleapis.com/css2?family=Montserrat:wght@400;600;700&family=Oswald:wght@600&display=swap" rel="stylesheet">
<style>
  :root {
    --backdrop: #d9d9d9;
    --paper: #ffffff;
    --navy: #0b3d7d;
    --ink: #2b2b2b;
    --muted: #6a6a6a;
    --heart-red: #d0161c;
    --sign-tint: #e8edf6;
  }
  * { margin: 0; padding: 0; box-sizing: border-box; }
  html, body { width: 1200px; height: 900px; overflow: hidden; }
  body {
    background: var(--backdrop);
    font-family: "Montserrat", Arial, sans-serif;
    color: var(--ink);
  }
  .letterhead {
    position: absolute;
    left: 294px; top: 17px;
    width: 612px; height: 866px;
    background: var(--paper);
    box-shadow: 0 2px 10px rgba(0,0,0,.18);
  }
  .brand-mark {
    position: absolute;
    left: 40px; top: 64px;
    width: 44px; height: 44px;
    border-radius: 50%;
    background: var(--heart-red);
  }
  .doctor-name {
    position: absolute;
    left: 134px; top: 44px;
    font-family: "Oswald", "Arial Narrow", sans-serif;
    font-weight: 600;
    font-size: 22px;
    font-variant: small-caps;
    letter-spacing: .3px;
    color: var(--navy);
    white-space: nowrap;
  }
  .credentials {
    position: absolute;
    left: 134px; top: 80px;
    font-size: 8.5px;
    color: var(--muted);
  }
  .specialty {
    position: absolute;
    left: 134px; top: 93px;
    font-size: 13.5px;
    font-weight: 700;
    color: var(--navy);
  }
  .letter-body {
    position: absolute;
    left: 88px; top: 287px;
    width: 437px;
    font-size: 10.8px;
    line-height: 13.5px;
    text-align: justify;
  }
  .letter-body p + p { margin-top: 13.5px; }
  .signature {
    position: absolute;
    left: 80px; top: 637px;
    width: 152px; height: 36px;
    background: var(--sign-tint);
    border-radius: 4px;
  }
  .signatory-role {
    position: absolute;
    left: 88px; top: 674px;
    font-size: 11px;
  }
  .consulting-band {
    position: absolute;
    left: 0; top: 726px;
    width: 100%; height: 16px;
    background: var(--navy);
    color: #fff;
    font-size: 9px;
    line-height: 16px;
    letter-spacing: 29px;
    text-align: center;
    padding-left: 29px;
  }
  .locations {
    position: absolute;
    top: 750px; left: 0;
    width: 100%;
  }
  .location {
    position: absolute;
    font-size: 7.8px;
    line-height: 12.5px;
    color: var(--muted);
    white-space: nowrap;
  }
  .location:nth-child(1) { left: 58px; }
  .location:nth-child(2) { left: 222px; }
  .location:nth-child(3) { left: 452px; }
  .location h3 {
    font-size: 8px;
    font-weight: 400;
    font-variant: small-caps;
    color: var(--navy);
  }
  .location .label { color: var(--navy); }
</style>
</head>
<body>
  <main class="letterhead">
    <div class="brand-mark" aria-hidden="true"></div>
    <h1 class="doctor-name">Dr Adaeze. O. Nwankwo</h1>
    <div class="credentials">M.B.B.S, F.M.C.P, F.R.A.C.P</div>
    <div class="specialty">Cardiologist</div>

    <section class="letter-body">
      <p>Letterhead samples are a great way of deciding what kind of letterhead you want to design for you and your company. The internet has a ton of great letterhead samples to browse through. Whether you want something simple, with just a couple lines of text of your business information, or something decorative and stunning, with photos and logos on the top and bottom of the page, it will be easy to find what you want, because there are samples online for basically any type of letterhead you could want.</p>
      <p>Any business could easily benefit from browsing through some letterhead samples, if only to get an idea for what kind of letterhead their company might want. Letterheads are just one of the tools that a business professional could use to help increase their customer base, and to really be memorable to everyone they write a letter to. Letterhead is quite an effective tool for marketing and advertising, but because it's such a simple and well known idea, it is often unfairly overlooked. Make sure you don't make that mistake, and make some letterhead samples of your own today.</p>
      <p>Whether you want to get new customers to remember you and become part of your clientele, or you just want to send out friendly reminders to your existing clients, customizing your own letterhead samples can really help you out. Try out some letterhead samples and you will not regret it, and I'm sure you will add a new tool to your business' arsenal of networking, marketing, and advertising tools.</p>
    </section>

    <div class="signature" role="img" aria-label="Handwritten signature of Marcus Hale"></div>
    <div class="signatory-role">company director</div>

    <div class="consulting-band">CONSULTING</div>

    <footer class="locations">
      <address class="location">
        <h3>The Riverside Specialist Centre</h3>
        18 Kestrel Road<br>
        Westbourne SA 5099<br>
        <span class="label">T:</span> 8310 2207<br>
        <span class="label">F:</span> 8310 2208<br>
        <span class="label">E:</span> cardiology@harbourcardio.com.au<br>
        <span class="label">Provider No:</span> 518264RA
      </address>
      <address class="location">
        <h3>Northern Heart &amp; Specialist Clinic</h3>
        Elmwood Districts Private Hospital<br>
        40-46 Marlow Road Ashfield Vale SA 5140<br>
        <span class="label">T:</span> 8355 6120<br>
        <span class="label">F:</span> 8355 6121<br>
        <span class="label">E:</span> cardiology@harbourcardio.com.au<br>
        <span class="label">Provider No:</span> 518264RB
      </address>
      <address class="location">
        <h3>Lakeview Regional Hospital</h3>
        9 Infirmary Road<br>
        Lakeview 5790<br>
        <span class="label">T:</span> 8690 4400<br>
        <span class="label">F:</span> 8310 2208<br>
        <span class="label">E:</span> cardiology@harbourcardio.com.au<br>
        <span class="label">Provider No:</span> 518264RC
      </address>
    </footer>
  </main>
</body>
</html>
```